Automotive component supplier needs a business card design

We need a business card design for our company called Velmar Global Components Ltd based in the UK. We are a supplier of interior and exterior components to premium car manufacturers such as Corvane Hale, Durrant Fyfe, Maxtorn and Valdessimo. We would like to see a modern business card design that uses the colour blue.

Target Market(s)

Premium automotive car manufacturers.

Industry/Entity Type

Automotive

Contact Information for Business Card

Company Name : Velmar Global Components Limited
Address: 17 Tamsey Yard, Upper Drisk, Warwick, CV31 8RJ, United Kingdom
Web Address : www.velmarparts-example.co.uk

Font styles to use
Other font styles liked:
• Helvetica

Colors
3176b5
0255a3
85acd3
cfdeed
cee9f5
85cae6
34a6d7
0692cd
9bcb3c

Requirements
Must have
• Clear company logo and a mixture of blue colours.
Nice to have
• A high quality modern image.
Should not have
• Multiple colours.

```html
<!DOCTYPE html>
<html lang="en">
<head>
<meta charset="utf-8">
<title>Velmar Global Components – Business Card</title>
<link href="https://fonts.googleapis.com/css2?family=Montserrat:wght@400;500;600;700&display=swap" rel="stylesheet">
<style>
  :root {
    --page-bg: #eeeeee;
    --card-bg: #ffffff;
    --brand-blue: #0692cd;
    --brand-blue-light: #34a6d7;
    --brand-green: #9bcb3c;
    --ink: #222222;
    --ink-soft: #555555;
    --rule: #9a9a9a;
  }
  * { box-sizing: border-box; margin: 0; padding: 0; }
  html, body {
    width: 1200px; height: 1000px; overflow: hidden;
    background: var(--page-bg);
    font-family: "Montserrat", Helvetica, Arial, sans-serif;
  }
  .canvas {
    position: relative; width: 1200px; height: 1000px;
    display: flex; align-items: center; justify-content: center; gap: 60px;
  }
  .card {
    position: relative; width: 520px; height: 318px;
    background: var(--card-bg);
    box-shadow: 0 6px 24px rgba(0,0,0,0.12);
    overflow: hidden;
  }
  .logo {
    display: flex; align-items: center; gap: 8px;
    color: var(--brand-blue); font-weight: 700; letter-spacing: 0.02em;
  }
  .logo-mark { width: 10px; height: 10px; background: var(--brand-green); flex: none; }

  /* Contact side */
  .card-contact .logo { position: absolute; left: 40px; top: 34px; }
  .card-contact .logo-name { font-size: 17px; line-height: 1.1; }
  .person { position: absolute; left: 40px; top: 92px; }
  .person-name { font-size: 17px; font-weight: 500; color: var(--ink); letter-spacing: 0.06em; }
  .person-role { margin-top: 6px; font-size: 9px; font-weight: 500; color: var(--ink-soft); letter-spacing: 0.1em; }
  .divider {
    position: absolute; left: 262px; top: 118px; width: 1px; height: 90px;
    background: var(--rule);
  }
  .contact-details {
    position: absolute; left: 284px; top: 118px; width: 216px;
    font-size: 11px; font-weight: 500; line-height: 1.45; color: var(--ink);
    font-style: normal;
  }
  .contact-details .gap { margin-top: 8px; }
  .card-contact .web {
    position: absolute; left: 40px; bottom: 40px;
    font-size: 11px; font-weight: 600; color: var(--ink);
  }

  /* Brand side */
  .band {
    position: absolute; left: 0; right: 0; top: 150px; height: 96px;
    background: linear-gradient(100deg, var(--brand-blue) 0%, var(--brand-blue-light) 55%, var(--brand-blue) 100%);
  }
  .card-brand .logo {
    position: absolute; left: 0; right: 0; top: 100px;
    justify-content: center; gap: 10px; z-index: 1;
  }
  .card-brand .logo-mark { width: 14px; height: 14px; }
  .card-brand .logo-name { font-size: 24px; line-height: 1.2; white-space: nowrap; }
  .card-brand .web {
    position: absolute; left: 0; right: 0; top: 190px; text-align: center;
    font-size: 12px; font-weight: 500; color: #ffffff; letter-spacing: 0.08em;
  }
</style>
</head>
<body>
<main class="canvas">
  <section class="card card-contact" aria-label="Business card, contact side">
    <div class="logo">
      <span class="logo-mark"></span>
      <span class="logo-name">VELMAR GLOBAL<br>COMPONENTS</span>
    </div>
    <div class="person">
      <p class="person-name">ALDEN ROE</p>
      <p class="person-role">GRAPHIC DESIGNER</p>
    </div>
    <span class="divider"></span>
    <address class="contact-details">
      <p>17 Tamsey Yard, Upper Drisk,<br>Warwick, CV31 8RJ,<br>United Kingdom</p>
      <p class="gap">info@velmarparts-example.co.uk</p>
      <p>+01 55501234</p>
      <p>+01 55501234</p>
    </address>
    <p class="web">www.velmarparts-example.co.uk</p>
  </section>

  <section class="card card-brand" aria-label="Business card, brand side">
    <div class="band"></div>
    <div class="logo">
      <span class="logo-mark"></span>
      <span class="logo-name">VELMAR GLOBAL COMPONENTS</span>
    </div>
    <p class="web">WWW.VELMARPARTS-EXAMPLE.CO.UK</p>
  </section>
</main>
</body>
</html>
```